"Eyebrow Threading Flyer Design"

We need a flyer design for a new service that will be provided in our established Beauty Salon in Toorak called "Threading". We provide all beauty services for our clients & would like to now introduce this very popular ancient method of hair removal.
Following are four "40% Off Threading Combo Packages" that will hopefully tempt new clients into our salon.
#Package 1- Eyebrow Threading plus Eyebrow Tint or Eyelash Tint Normally $53 Now $32
#Package 2- Eyebrow Threading plus Full Set Mink Lash Extensions
Normally $208 Now $125
#Package 3- Eyebrow Threading plus Glossa Manicure Or Pedicure
Normally $128 Now $77
#Package 4- Eyebrow Threading plus Collagen Facial
Normally $148 Now $89
We would like to see designs that use pink with whit or black to suit logo & business name & final design should be girly/feminine 7 fun.
On the back we would like the following details:
Velvet Dawn Beauty, "Lindell Court", shop 7, 418 Marlowe Street, 3187
Tel: 03 9471 2360, Email: info@velvetdawnbeauty.example, Web: www.velvetdawnbeauty.example
A map of exact location and business hours:
Mon 9am to 5pm, Tue 9am to 6pm, Wed 9am to 6pm, Thu 9am to 8pm, Fri 9am to 6pm, sat 9am to 5pm

Target Market(s)

Women between the ages of 20 to 60 years of age

Industry/Entity Type

Hair

Font styles to use
Script

Colors
e34297
000000

Requirements
Must have
• Pink and black or pink and white colors
Should not have
• Fake looking eyelashes displayed

```html
<!DOCTYPE html>
<html lang="en">
<head>
<meta charset="utf-8">
<title>Velvet Dawn Beauty – Threading Flyer</title>
<link rel="stylesheet" href="https://fonts.googleapis.com/css2?family=Kaushan+Script&family=Cinzel:wght@400&family=Arimo:wght@400;700&display=swap">
<style>
  :root {
    --pink: #e34297;
    --ink: #111111;
    --body-text: #3d3430;
    --band: #4e3426;
    --lavender: #c9c8e3;
    --lavender-soft: #eceef8;
    --peach: #f6b766;
    --emblem-grey: #d9d9dc;
    --panel-edge: #9a9a9a;
    --page: #ffffff;
  }
  * { margin: 0; padding: 0; box-sizing: border-box; }
  html, body {
    width: 1200px; height: 1021px; overflow: hidden;
    background: var(--page);
  }
  .canvas { position: relative; width: 1200px; height: 1021px; }

  .flyer {
    position: absolute; top: 91px; width: 379px; height: 818px;
    background: var(--page); border: 1px solid var(--panel-edge); overflow: hidden;
  }
  .flyer--front { left: 185px; }
  .flyer--back { left: 600px; border-color: #333; }

  .swirl-backdrop {
    position: absolute; inset: 0;
    background: radial-gradient(ellipse at 30% 40%, var(--lavender-soft) 0%, rgba(236,238,248,0.5) 45%, rgba(255,255,255,0) 80%);
  }
  .flyer--back .swirl-backdrop {
    background: radial-gradient(ellipse at 75% 55%, #e6e6f3 0%, rgba(230,230,243,0.5) 50%, rgba(255,255,255,0) 85%);
  }

  .brand-mark {
    position: absolute; width: 96px; height: 96px; border-radius: 50%;
    background: var(--emblem-grey);
  }
  .flyer--front .brand-mark { left: 138px; top: 56px; }
  .flyer--back .brand-mark { left: 212px; top: 176px; width: 90px; height: 90px; }

  .brand-name {
    position: absolute; font-family: "Cinzel", serif; font-weight: 400;
    color: var(--pink); font-size: 24px; line-height: 30px; letter-spacing: 0.5px; white-space: nowrap;
  }
  .flyer--front .brand-name { left: 0; right: 0; top: 180px; text-align: center; }
  .flyer--back .brand-name { right: 20px; top: 302px; font-size: 19px; }

  .package-list { position: absolute; left: 27px; top: 251px; }
  .package { height: 87px; }
  .package__title {
    font-family: "Kaushan Script", cursive; color: var(--pink);
    font-size: 23px; line-height: 26px;
  }
  .package__detail {
    font-family: "Arimo", Arial, sans-serif; font-size: 12.5px; color: var(--ink);
    line-height: 14px; margin-left: -2px;
  }
  .package__price {
    font-family: "Kaushan Script", cursive; color: var(--ink);
    font-size: 21px; line-height: 28px;
  }

  .floral { position: absolute; }
  .floral--front {
    left: 0; right: 0; top: 585px; height: 209px;
    background: linear-gradient(100deg, rgba(201,200,227,0.55) 0%, rgba(201,200,227,0.8) 35%, rgba(246,183,102,0.7) 60%, rgba(201,200,227,0.4) 100%);
    border-radius: 60% 60% 0 0 / 30% 30% 0 0;
  }
  .floral--back {
    left: 0; top: 0; width: 160px; height: 575px;
    background: linear-gradient(170deg, rgba(246,183,102,0.55) 0%, rgba(201,200,227,0.8) 35%, rgba(246,183,102,0.7) 65%, rgba(201,200,227,0.75) 90%);
    border-radius: 0 50% 40% 0 / 0 20% 15% 0;
  }

  .base-band {
    position: absolute; left: 0; right: 0; bottom: 0; height: 23px; background: var(--band);
  }

  .contact { position: absolute; left: 30px; top: 594px; font-style: normal; }
  .contact__lead {
    font-family: "Kaushan Script", cursive; color: var(--pink); font-size: 14px; line-height: 18px;
  }
  .contact__line {
    font-family: "Arimo", Arial, sans-serif; color: var(--body-text); font-size: 14px; line-height: 18px;
  }
  .hours { position: absolute; left: 30px; top: 703px; }

  .panel-label {
    position: absolute; top: 940px; width: 100px; text-align: center;
    font-family: "Arimo", Arial, sans-serif; font-weight: 700; font-size: 14px; color: var(--ink);
  }
  .panel-label--front { left: 320px; }
  .panel-label--back { left: 739px; }
</style>
</head>
<body>
<div class="canvas">

  <section class="flyer flyer--front">
    <div class="swirl-backdrop" role="img" aria-label="Faint lavender swirl pattern"></div>
    <div class="brand-mark"></div>
    <div class="brand-name">Velvet Dawn Beauty</div>

    <div class="package-list">
      <div class="package">
        <div class="package__title">Package 1</div>
        <div class="package__detail">Eyebrow Threading plus Eyebrow Tint or Eyelash Tint</div>
        <div class="package__price">Normally $53 Now $32</div>
      </div>
      <div class="package">
        <div class="package__title">Package 2</div>
        <div class="package__detail">Eyebrow Threading plus Full Set Mink Lash Extensions</div>
        <div class="package__price">Normally $208 Now $125</div>
      </div>
      <div class="package">
        <div class="package__title">Package 3</div>
        <div class="package__detail">Eyebrow Threading plus Glossa Manicure Or Pedicure</div>
        <div class="package__price">Normally $128 Now $77</div>
      </div>
      <div class="package">
        <div class="package__title">Package 4</div>
        <div class="package__detail">Eyebrow Threading plus Collagen Facial</div>
        <div class="package__price">Normally $148 Now $89</div>
      </div>
    </div>

    <div class="floral floral--front" role="img" aria-label="Illustration of lavender lily, peach carnation and line-drawn butterflies on curling vines"></div>
    <div class="base-band"></div>
  </section>

  <section class="flyer flyer--back">
    <div class="swirl-backdrop" role="img" aria-label="Faint lavender swirl pattern"></div>
    <div class="floral floral--back" role="img" aria-label="Illustration of lavender lily, peach and lavender peonies, and butterflies on curling vines"></div>
    <div class="brand-mark"></div>
    <div class="brand-name">Velvet Dawn Beauty</div>

    <address class="contact">
      <div class="contact__lead">Velvet Dawn Beauty, "Lindell Court", shop 7,</div>
      <div class="contact__lead">418 Marlowe Street, 3187</div>
      <div class="contact__line">Tel: 03 9471 2360,</div>
      <div class="contact__line">Email: info@velvetdawnbeauty.example,</div>
      <div class="contact__line">Web: www.velvetdawnbeauty.example</div>
    </address>

    <div class="hours">
      <div class="contact__lead">A map of exact location and business hours:</div>
      <div class="contact__line">Mon 9am to 5pm, Tue 9am to 6pm,</div>
      <div class="contact__line">Wed 9am to 6pm, Thu 9am to 8pm,</div>
      <div class="contact__line">Fri 9am to 6pm, sat 9am to 5pm</div>
    </div>

    <div class="base-band"></div>
  </section>

  <div class="panel-label panel-label--front">Front</div>
  <div class="panel-label panel-label--back">Back</div>
</div>
</body>
</html>
```